Shopping center investment profile

We need to design a two-page 8.5" x 11" brochure that can be used as a template for profiling our shopping centers and demonstrating our track record to investors.

Our company (KVM Real Estate Investments) owns retail shopping centers in the southwestern United States. Our website is www.kvmtrh.example, but we will be redesigning and modernizing the website and logo in the near future, so please do not use the color schemes or framework of the website for the brochure.

Our investors are institutional and high net worth investors who typically have an existing relationship with our company. They are determining whether to invest multi-millions of dollars in a shopping center opportunity, so the brochure needs to be professional, very high quality and provide key information about the specific property.
Updates

Additional guidance on color scheme:

We would like to see a Blue (something like Hex #5A61BC) and Gold (Hex #EDB215) or (Hex #DDA24B) color scheme with some Black accents 

Thank you!

Target Market(s)

Our target audiences are institutional investors, high net-worth individuals, financial firms and medium to large commercial real estate companies.

Industry/Entity Type

Investment

Requirements
Must have
• Clean and modern look with corresponding fonts and colors.
• Incorporates the information found in the attached "Marlowe Crossing profile" Pages or PDF file.
• Final file design files that can be modified easily
Nice to have
• Two examples of industry brochures are attached. These are examples of the professional quality that we are looking for, not necessarily the design or format.

```html
<!DOCTYPE html>
<html lang="en">
<head>
<meta charset="utf-8">
<title>KVM Real Estate Investments – Shopping Center Investment Profile</title>
<link rel="stylesheet" href="https://fonts.googleapis.com/css2?family=Source+Sans+3:wght@400;600&display=swap">
<style>
  :root {
    --gold: #EDB215;
    --gold-soft: #DDA24B;
    --gold-pale: #F0C98C;
    --blue: #5A61BC;
    --black: #0A0A0A;
    --grey: #D8D8D8;
    --ink: #2A2520;
    --white: #FFFFFF;
    --backdrop: #E6E6E6;
    --sky: #8FA9CF;
    --building: #9B7B63;
  }
  * { box-sizing: border-box; margin: 0; padding: 0; }
  html, body { width: 1200px; height: 847px; overflow: hidden; }
  body {
    background: var(--backdrop);
    font-family: "Source Sans 3", "Myriad Pro", sans-serif;
    color: var(--ink);
    display: flex; align-items: center; justify-content: center; gap: 24px;
  }
  .page { width: 386px; height: 500px; position: relative; overflow: hidden; box-shadow: 0 2px 10px rgba(0,0,0,.12); }
  .spread { display: flex; }

  /* Cover */
  .cover { background: var(--gold); display: flex; flex-direction: column; }
  .cover-title { background: var(--gold-soft); height: 120px; padding: 26px 18px; color: var(--white); font-size: 22px; line-height: 1.15; font-weight: 400; }
  .cover-photo { position: relative; height: 218px; background: linear-gradient(180deg, var(--sky) 0%, #BFD0E6 48%, var(--building) 62%, #5C5D63 100%); }
  .grid-lines { position: absolute; inset: 0; }
  .cover-blocks { display: grid; grid-template-columns: repeat(4, 1fr); height: 76px; }
  .cover-blocks .blue { background: var(--blue); grid-column: 3; border: 1px solid var(--gold-soft); }
  .cover-blocks .black { background: var(--black); grid-column: 4; border: 1px solid var(--gold-soft); }
  .tagline { margin-top: auto; padding: 0 16px 26px; text-align: right; font-size: 16px; line-height: 1.2; }
  .tagline span { display: block; }
  .tagline .first { text-align: left; padding-left: 88px; }

  /* Inside */
  .section-head { height: 24px; padding: 0 12px; display: flex; align-items: center; font-size: 13px; font-weight: 600; }
  .head-pale { background: var(--gold-pale); }
  .head-gold { background: var(--gold); }
  .bullets { list-style: none; padding: 6px 12px; font-size: 8.4px; line-height: 1.5; }
  .bullets li::before { content: "• "; }
  .bullets li { padding-left: 6px; text-indent: -6px; margin-bottom: 2px; }
  .gold-body { background: var(--gold-soft); }
  .opportunity { height: 150px; }
  .center-photo { height: 148px; background: linear-gradient(180deg, var(--sky) 0%, #C8D6E8 40%, var(--building) 58%, #55565C 100%); }
  .results { height: 154px; }

  .right-page { background: var(--grey); display: flex; flex-direction: column; }
  .challenges { background: var(--blue); color: var(--white); padding: 8px 12px; font-size: 7.6px; line-height: 1.45; height: 160px; }
  .challenges p { margin-bottom: 5px; }
  .data-table { width: 100%; border-collapse: collapse; font-size: 7.4px; }
  .data-table td { padding: 2px 12px; }
  .data-table td:last-child { text-align: right; }
  .summary { padding: 18px 0 10px; height: 140px; }
  .investment { padding: 12px 0; flex: 1; }
  .split td { padding-top: 14px; }
</style>
</head>
<body>

<section class="page cover">
  <h1 class="cover-title">KVM Real Estate<br>Investments</h1>
  <div class="cover-photo" role="img" aria-label="Rendering of the shopping center storefronts and parking lot under a blue sky">
    <svg class="grid-lines" viewBox="0 0 386 218" preserveAspectRatio="none" aria-hidden="true">
      <g stroke="#DDA24B" stroke-width="2">
        <line x1="96.5" y1="0" x2="96.5" y2="218"/>
        <line x1="193" y1="0" x2="193" y2="218"/>
        <line x1="289.5" y1="0" x2="289.5" y2="218"/>
        <line x1="0" y1="72.7" x2="386" y2="72.7"/>
        <line x1="0" y1="145.3" x2="386" y2="145.3"/>
      </g>
    </svg>
  </div>
  <div class="cover-blocks"><div class="blue"></div><div class="black"></div></div>
  <p class="tagline"><span class="first">making communities better</span><span>one property at a time</span></p>
</section>

<div class="spread">
  <section class="page left-page">
    <h2 class="section-head head-pale">Opportunity</h2>
    <ul class="bullets gold-body opportunity">
      <li>Bank owned property with attractive purchase price</li>
      <li>Strong relationship with seller's broker and decision makers</li>
      <li>Redevelopment upside with management and leasing</li>
      <li>No major renovations required</li>
      <li>Alder Springs location has very strong population, education and income demographics</li>
      <li>Adjacent to premier 2,500-residence master planned community of Willow Shore Lakes</li>
      <li>Strong employment area with the new Northgate Regional hospital and the adjacent Halvorsen Cancer center</li>
    </ul>
    <div class="center-photo" role="img" aria-label="Rendering of the shopping center facade with signage, trees and parked cars"></div>
    <h2 class="section-head head-pale">Results</h2>
    <ul class="bullets gold-body results">
      <li>Stabilized the shopping center within three years, producing excellent results for investors</li>
      <li>Transformed the center into a vibrant destination that the surrounding community is excited about</li>
      <li>Transitioned legacy tenants to upgrade the business operators</li>
      <li>Reduced the shopping center's operating expenses by replacing vendors and appealing property taxes</li>
    </ul>
  </section>

  <section class="page right-page">
    <h2 class="section-head head-gold">Challenges and Solutions</h2>
    <div class="challenges">
      <p>• Nationwide vacancy rate - KVM did significant due diligence on the property before purchasing the asset, and determined that the location is an A/A-; Tenant improvement and leasing commissions were reserved in order to attract national and regional tenants</p>
      <p>• Size of Anchor space - KVM determined that a family-friendly entertainment venue would best serve the demographics in the area instead of another grocer; KVM sought out an experienced operator in Fun Alley, who has multiple locations in three states</p>
      <p>• Curb Appeal - With vacancy and a stigma attached to the center, KVM had to change the center's appeal to the community. KVM worked hand in hand with the Town of Alder Springs and the Willow Shore Lakes community association to paint the center, upgrade landscaping and add new and larger monument signs</p>
    </div>
    <h2 class="section-head head-gold">Summary</h2>
    <div class="summary">
      <table class="data-table">
        <tr><td>Property Type</td><td>Shopping Center</td></tr>
        <tr><td>Size</td><td>79,490 sq ft</td></tr>
        <tr><td>Purchased</td><td>April 2007</td></tr>
        <tr><td>Total Investment</td><td>$X,XXX,XXX</td></tr>
        <tr><td>Purchase Occupancy</td><td>8.39%</td></tr>
        <tr><td>Current Occupancy</td><td>97.29%</td></tr>
        <tr><td>Projected 5-year IRR (Unleveraged)</td><td>XX.XX%</td></tr>
      </table>
    </div>
    <h2 class="section-head head-gold">Investment Information</h2>
    <div class="investment">
      <table class="data-table">
        <tr><td>Purchase Price</td><td>$X,XXX,XXX</td></tr>
        <tr><td>Sponsor Acquisition Fee</td><td>$XX,XXX</td></tr>
        <tr><td>Painting and Landscape</td><td>$XXX,XXX</td></tr>
        <tr><td>TI/LC Reserve</td><td>$XXX,XXX</td></tr>
        <tr><td>Operating Expenses</td><td>$X,XXX,XXX</td></tr>
        <tr><td>Total Cash Investment</td><td>$XXX,XXX</td></tr>
        <tr class="split"><td>Investor / Sponsor Split</td><td>XX% / XX%</td></tr>
      </table>
    </div>
  </section>
</div>

</body>
</html>
```